Graphic Design for Flavoured Drink product

I need a packaging design for flavoured drinks product.
The product is a mix of Sparkling Natural Mineral Water (from France) with other flavouring.

There will be various flavours i.e. apple, orange, strawberry, etc.
However, you may design the product using one sample flavour first, as the designs of other flavours could be adjusted afterwards.

The temporary product name is: QUIVLO

I want the product design to be something 'fun' and 'colourful'.
The design concept could be anything depends on your imagination.
Basically, I want you to be creative in designing the logo and the overall graphic design for the label.

- Create something different. Something extraordinary -

Thank you and Good Luck!

Additional:

The measurement is 20cm (Length) x 10cm (Height).

The target customers are young audiences (10 years - 35 years old).

I am hoping to have a product design that can stand out in the supermarket shelf.
It must be eye catchy and attractive.

Thank you,
Marcus

-PLEASE REFER TO DESIGN SAMPLE ATTACHED TO HAVE A BETTER UNDERSTANDING FOR THE PRODUCT CONCEPT-

Reason: I havent found any satisfactory designs so far. Please submit much better quality designs. Thank you, Marcus

```html
<!DOCTYPE html>
<html lang="en">
<head>
<meta charset="utf-8">
<title>QUIVLO Apple Label</title>
<link href="https://fonts.googleapis.com/css2?family=Julius+Sans+One&family=Michroma&display=swap" rel="stylesheet">
<style>
  :root {
    --ink: #2e2e2e;
    --band: #333333;
    --green: #8dc63f;
    --green-deep: #5f9a1c;
    --green-mid: #7fb93a;
    --green-light: #c6e58f;
    --splash: #dfe6ec;
    --paper: #ffffff;
    --rule: #1a1a1a;
  }
  * { margin: 0; padding: 0; box-sizing: border-box; }
  html, body { width: 1200px; height: 599px; overflow: hidden; background: var(--paper); }
  .label { position: relative; width: 1200px; height: 599px; background: var(--paper); overflow: hidden; }
  .top-band, .bottom-band { position: absolute; left: 0; width: 1200px; z-index: 2; }
  .top-band { top: 0; height: 90px; }
  .bottom-band { bottom: 0; height: 40px; }
  .flavour {
    position: absolute; left: 850px; top: 8px; z-index: 3;
    font-family: "Michroma", sans-serif; font-size: 23px; line-height: 1; letter-spacing: 2px;
    color: var(--green);
  }
  .panel {
    position: absolute; border: 1.5px solid var(--rule);
    display: flex; align-items: center; justify-content: center; text-align: center;
    font-family: "Michroma", sans-serif; font-size: 12px; line-height: 1.75;
    letter-spacing: 2px; text-transform: uppercase; color: var(--green);
  }
  .panel--nutrition { left: 32px; top: 104px; width: 229px; height: 444px; }
  .panel--info { left: 279px; top: 104px; width: 326px; height: 292px; }
  .panel--distributor { left: 279px; top: 417px; width: 326px; height: 131px; }
  .product-photo {
    position: absolute; left: 650px; top: 225px; width: 550px; height: 335px; z-index: 1;
    background:
      linear-gradient(to right, var(--paper) 0%, rgba(255,255,255,0) 38%),
      linear-gradient(to bottom, var(--paper) 0%, rgba(255,255,255,0) 22%),
      radial-gradient(ellipse 60% 85% at 80% 70%, var(--green-deep) 0%, var(--green-mid) 30%, var(--green) 48%, var(--green-light) 66%, var(--splash) 86%, var(--splash) 100%);
  }
  .brand {
    position: absolute; left: 740px; top: 124px; width: 340px; text-align: center;
    color: var(--ink); z-index: 2;
  }
  .brand__name {
    font-family: "Julius Sans One", sans-serif; font-size: 74px; line-height: 1;
    letter-spacing: 0; font-weight: 400;
  }
  .brand__tagline {
    font-family: "Julius Sans One", sans-serif; font-size: 20px; line-height: 1;
    margin-top: 2px; letter-spacing: 0.5px; text-transform: uppercase;
  }
</style>
</head>
<body>
<main class="label">
  <svg class="top-band" viewBox="0 0 1200 90" aria-hidden="true">
    <path d="M0 0 H1200 V66 C900 62 640 46 0 60 Z" fill="#bdbdbd"/>
    <path d="M0 0 H1200 V60 C900 56 640 40 0 54 Z" fill="var(--green)"/>
    <path d="M0 0 H1200 V46 C900 44 620 24 0 44 Z" fill="var(--band)"/>
  </svg>
  <div class="flavour">APPLE</div>

  <section class="panel panel--nutrition"><p>Nutrition<br>Facts</p></section>
  <section class="panel panel--info"><p>Information<br>about your<br>mineral water</p></section>
  <section class="panel panel--distributor"><p>Distributed by<br>company website<br>phone number<br>recyclables</p></section>

  <div class="product-photo" role="img" aria-label="Photo of a green apple with a splash of water"></div>

  <div class="brand">
    <h1 class="brand__name">QUIVLO</h1>
    <p class="brand__tagline">Flavoured Mineral Water</p>
  </div>

  <svg class="bottom-band" viewBox="0 0 1200 40" aria-hidden="true">
    <rect x="0" y="2" width="1200" height="7" fill="var(--green)"/>
    <rect x="0" y="12" width="1200" height="28" fill="var(--band)"/>
  </svg>
</main>
</body>
</html>
```